Bref créative
BrindleWorks Stationery
Package
Use same font as used in my logo
Myriad
Professional
Marc T. Delvaux
Founder
418 Quarry Lane
Elmsbury, NH 03999
marc.delvaux@brindleworks-mail.com
www.brindleworks-mail.com

```html
<!DOCTYPE html>
<html lang="en">
<head>
<meta charset="utf-8">
<title>BrindleWorks Business Card</title>
<link href="https://fonts.googleapis.com/css2?family=Source+Sans+3:wght@300;400;600;700&display=swap" rel="stylesheet">
<style>
  :root {
    --stage: #e4e5e7;
    --card-dark: #1c1c1e;
    --card-light: #ffffff;
    --ink: #2a2a2c;
    --ink-soft: #555558;
    --muted: #9a9a9e;
    --accent-red: #e4262a;
    --accent-black: #1a1a1a;
    --icon-bg: #333336;
    --rule: #c9c9cc;
  }
  * { box-sizing: border-box; margin: 0; padding: 0; }
  html, body {
    width: 1200px; height: 864px; overflow: hidden;
    background: var(--stage);
    font-family: "Source Sans 3", "Myriad Pro", sans-serif;
  }
  .stage {
    width: 1200px; height: 864px;
    display: flex; align-items: center; justify-content: center; gap: 60px;
  }
  .card {
    position: relative;
    width: 520px; height: 300px;
    border-radius: 18px;
    overflow: hidden;
    box-shadow: 0 10px 28px rgba(0,0,0,0.18);
  }

  /* Back side */
  .card--back {
    background: var(--card-dark);
    display: flex; flex-direction: column; align-items: center; justify-content: center;
    gap: 26px;
  }
  .brand-mark { display: flex; align-items: center; gap: 12px; }
  .brand-mark__dot {
    width: 34px; height: 34px; border-radius: 50%;
    background: var(--muted);
  }
  .brand-mark__name {
    font-size: 36px; font-weight: 400; color: #ffffff; letter-spacing: -0.5px;
  }
  .back-url {
    font-size: 13px; color: var(--muted); letter-spacing: 4px;
  }

  /* Front side */
  .card--front { background: var(--card-light); }
  .front-swoosh { position: absolute; inset: 0; }
  .front-logo {
    position: absolute; left: 30px; top: 34px;
    display: flex; align-items: center; gap: 12px;
  }
  .front-logo__dot {
    width: 46px; height: 46px; border-radius: 50%;
    background: var(--ink);
  }
  .front-logo__name {
    font-size: 50px; font-weight: 400; color: var(--ink); letter-spacing: -1px; line-height: 1;
  }
  .front-details {
    position: absolute; left: 30px; top: 120px;
    display: flex; align-items: flex-start;
  }
  .person {
    text-align: right; padding-right: 14px; padding-top: 4px;
    border-right: 1.5px solid var(--rule);
    min-width: 150px; height: 74px;
  }
  .person__name { font-size: 16px; font-weight: 700; color: var(--ink); }
  .person__role { font-size: 12px; font-weight: 400; color: var(--ink-soft); margin-top: 1px; }
  .contact-list { list-style: none; padding-left: 12px; display: flex; flex-direction: column; gap: 6px; }
  .contact-list__item {
    display: flex; align-items: center; gap: 7px;
    font-size: 11.5px; color: var(--ink-soft);
  }
  .contact-icon {
    width: 15px; height: 15px; border-radius: 50%;
    background: var(--icon-bg);
    display: flex; align-items: center; justify-content: center; flex: none;
  }
  .address {
    position: absolute; left: 30px; top: 212px;
    font-size: 12px; color: var(--ink-soft);
  }
</style>
</head>
<body>
<main class="stage">

  <section class="card card--back" aria-label="Business card back">
    <div class="brand-mark">
      <span class="brand-mark__dot"></span>
      <span class="brand-mark__name">BrindleWorks</span>
    </div>
    <p class="back-url">www.BrindleWorks-mail.com</p>
  </section>

  <section class="card card--front" aria-label="Business card front">
    <svg class="front-swoosh" viewBox="0 0 520 300" width="520" height="300" aria-hidden="true">
      <path d="M240 300 C 360 270, 450 210, 520 130 L 520 300 Z" fill="var(--accent-black)"/>
      <path d="M300 300 C 400 280, 470 230, 520 180 L 520 300 Z" fill="var(--accent-red)"/>
      <path d="M150 300 C 300 285, 420 240, 520 175 L 520 200 C 420 262, 300 296, 200 300 Z" fill="var(--accent-red)"/>
    </svg>

    <div class="front-logo">
      <span class="front-logo__dot"></span>
      <span class="front-logo__name">BrindleWorks</span>
    </div>

    <div class="front-details">
      <div class="person">
        <p class="person__name">Marc T. Delvaux</p>
        <p class="person__role">Founder</p>
      </div>
      <ul class="contact-list">
        <li class="contact-list__item">
          <span class="contact-icon">
            <svg width="9" height="9" viewBox="0 0 24 24" aria-hidden="true"><path fill="#fff" d="M6.6 10.8a15 15 0 0 0 6.6 6.6l2.2-2.2c.3-.3.7-.4 1-.2 1.1.4 2.3.6 3.6.6.6 0 1 .4 1 1V20c0 .6-.4 1-1 1A17 17 0 0 1 3 4c0-.6.4-1 1-1h3.5c.6 0 1 .4 1 1 0 1.3.2 2.5.6 3.6.1.3 0 .7-.2 1z"/></svg>
          </span>
          555-201-0142
        </li>
        <li class="contact-list__item">
          <span class="contact-icon">
            <svg width="9" height="9" viewBox="0 0 24 24" aria-hidden="true"><rect x="3" y="6" width="18" height="12" rx="1" fill="none" stroke="#fff" stroke-width="2.5"/><path d="M3 7l9 6 9-6" fill="none" stroke="#fff" stroke-width="2.5"/></svg>
          </span>
          marc.delvaux@brindleworks-mail.com
        </li>
        <li class="contact-list__item">
          <span class="contact-icon">
            <svg width="9" height="9" viewBox="0 0 24 24" aria-hidden="true"><circle cx="12" cy="12" r="9" fill="none" stroke="#fff" stroke-width="2.5"/><path d="M3 12h18M12 3c3 3 3 15 0 18M12 3c-3 3-3 15 0 18" fill="none" stroke="#fff" stroke-width="2"/></svg>
          </span>
          www.brindleworks-mail.com
        </li>
      </ul>
    </div>

    <p class="address">418 Quarry Lane Elmsbury, NH 03999</p>
  </section>

</main>
</body>
</html>
```